Flyer for Lawnmowing and gardening business

We are a lawn mowing and gardening business needing a flyer designed listing our services and business info.
The flyer should include all business information and contact details as below.

Lawn mowing
Gardening
Green waste removal
Pruning
Weeding
Vegetable Garden Creation

Phone number:0481657240

As well as the logo provided

Target Market(s)

Local people wanting someone to care for their garden.

Industry/Entity Type

Gardener

Font styles to use
Serif

Requirements
Must have
• Business Logo
• All business info and services provided. EG
• Lawn mowing
• Gardening
• Green waste removal
• Pruning
• Weeding
• Vegetable Garden Creation
• Phone number:0481657240
Nice to have
• Earthy tones, clean and simple flyer design

```html
<!DOCTYPE html>
<html lang="en">
<head>
<meta charset="utf-8">
<title>Greenhollow Yard – Lawn Mowing &amp; Garden Care Flyer</title>
<link rel="stylesheet" href="https://fonts.googleapis.com/css2?family=Cinzel:wght@500;600&family=PT+Sans:wght@400;700&display=swap">
<style>
  :root {
    --parchment: #efe2c0;
    --parchment-light: #f6ecd2;
    --parchment-edge: #dcc79a;
    --leaf-green: #4f8a2a;
    --leaf-light: #8cbf3f;
    --bark-brown: #4a2e17;
    --ink: #2b2a22;
    --phone-ink: #3a3a36;
    --hedge-dark: #2f5a1e;
    --hedge-mid: #5f9a34;
    --turf-mid: #6e9f3a;
    --soil: #8a6a43;
  }
  * { margin: 0; padding: 0; box-sizing: border-box; }
  html, body { width: 706px; height: 1200px; overflow: hidden; }
  body { background: var(--parchment); }

  .flyer {
    position: relative;
    width: 706px;
    height: 1200px;
    overflow: hidden;
    background:
      radial-gradient(ellipse at 50% 55%, var(--parchment-light) 0%, var(--parchment) 55%, var(--parchment-edge) 100%);
  }

  .header-art { position: absolute; top: 0; left: 0; width: 706px; height: 440px; }

  .brand {
    position: absolute;
    top: 440px;
    left: 0;
    width: 100%;
    text-align: center;
  }
  .brand-mark {
    display: block;
    width: 62px; height: 62px;
    margin: 0 auto 14px;
    border-radius: 50%;
    background: var(--leaf-green);
  }
  .brand-name {
    font-family: "Cinzel", serif;
    font-weight: 600;
    font-size: 46px;
    letter-spacing: 1px;
    color: var(--leaf-green);
    line-height: 1.05;
  }
  .brand-tagline {
    font-family: "Cinzel", serif;
    font-weight: 500;
    font-size: 22px;
    letter-spacing: 1px;
    color: var(--leaf-green);
    margin-top: 4px;
  }

  .services {
    position: absolute;
    top: 640px;
    left: 0;
    width: 100%;
    list-style: none;
    text-align: center;
    font-family: "PT Sans", sans-serif;
    font-size: 37px;
    line-height: 49px;
    color: var(--ink);
  }

  .gallery {
    position: absolute;
    top: 935px;
    left: 36px;
    width: 634px;
    height: 150px;
    display: flex;
    gap: 18px;
  }
  .gallery-photo {
    flex: 1;
    border-radius: 4px;
  }
  .gallery-photo.mower {
    background: linear-gradient(135deg, var(--turf-mid) 0%, #4d7d2a 45%, #b8322a 55%, #5d8c30 100%);
  }
  .gallery-photo.turf {
    background: linear-gradient(160deg, var(--soil) 0%, #a7895c 35%, var(--turf-mid) 60%, #4f7f2b 100%);
  }

  .contact {
    position: absolute;
    top: 1120px;
    left: 0;
    width: 100%;
    text-align: center;
    font-family: "PT Sans", sans-serif;
    font-weight: 700;
    font-size: 46px;
    color: var(--phone-ink);
  }
</style>
</head>
<body>
  <main class="flyer">
    <svg class="header-art" viewBox="0 0 706 440" aria-hidden="false">
      <defs>
        <linearGradient id="hedge-tone" x1="0" y1="0" x2="0.3" y2="1">
          <stop offset="0" stop-color="var(--hedge-dark)"/>
          <stop offset="0.5" stop-color="var(--hedge-mid)"/>
          <stop offset="1" stop-color="#3f7224"/>
        </linearGradient>
      </defs>
      <path class="curve-brown" d="M0 0 H706 V170 C640 330 470 415 250 415 C150 415 60 395 0 370 Z" fill="var(--bark-brown)"/>
      <path class="curve-green" d="M706 0 V190 C690 230 660 270 630 300 C670 240 690 150 680 0 Z" fill="var(--leaf-light)"/>
      <path class="header-photo" role="img" aria-label="Photo of a gardener trimming a hedge with a petrol hedge trimmer"
            d="M0 0 H668 C690 130 640 280 520 340 C430 385 330 400 220 395 C130 390 55 375 0 355 Z"
            fill="url(#hedge-tone)"/>
    </svg>

    <header class="brand">
      <span class="brand-mark"></span>
      <h1 class="brand-name">Greenhollow Yard</h1>
      <p class="brand-tagline">Lawn Mowing &amp; Garden Care</p>
    </header>

    <ul class="services">
      <li>Lawn mowing</li>
      <li>Gardening</li>
      <li>Green waste removal</li>
      <li>Pruning</li>
      <li>Weeding</li>
      <li>Vegetable Garden Creation</li>
    </ul>

    <section class="gallery">
      <div class="gallery-photo mower" role="img" aria-label="Photo of a red lawn mower cutting grass"></div>
      <div class="gallery-photo turf" role="img" aria-label="Photo of a gardener laying rolls of fresh turf"></div>
    </section>

    <p class="contact">Call: 0481657240</p>
  </main>
</body>
</html>
```